Company Values Graphic

We are looking for a design of our company values that can be used in a variety of places including our website, mousepads, office posters, business cards, etc.

Notes:
- We'd rather have icons/art than photographs on the poster.... so more like an infographic
- The core value group headings are not required, but can be included if you think grouping the values works for your design
- We have a logo for our software product but that logo is not required
- We don't need/want clever images to accompany each value, but some images are fine
- BrisKel logo attached
- BrisKel colors are attached
- BrisKel logo is Nunito Sans ExtraBold 800
- BrisKel website uses Roboto

Our Values - Who we will work with (and who we will not)
The right set of values are essential to building and maintaining a culture that we all wake up eager to be a part of each day. They are foundational to all hiring and firing decisions. They attract the right people and repel the wrong ones.

BE HELPFUL
Make every person and place better because you are there.
Deliver wow with every interaction.

BE HUMBLE
Listen with every muscle.
Passionately help others first.
Seek first to understand.

BE HONEST
Earn trust every day.
Be open and direct.
Treat everyone with fairness and respect.

BE HUMAN
Celebrate passion and action.
Create an environment where people are authentic.
Hire great people and expect a lot from them

BE COURAGEOUS
Dare mighty things.
Make and honor commitments.
All great things start with a small act of courage applied at the right moment.

```html
<!DOCTYPE html>
<html lang="en">
<head>
<meta charset="utf-8">
<title>BrisKel — Our Values</title>
<link href="https://fonts.googleapis.com/css2?family=Poppins:wght@400;700;800&display=swap" rel="stylesheet">
<style>
  :root {
    --backdrop: #8a8a8a;
    --ink-dark: #1e1e1e;
    --title-grey: #444444;
    --paper: #ffffff;
    --text: #222222;
    --amber: #ff9900;
    --orange: #ff5a00;
    --red: #ff0000;
    --amber-deep: #e88a0c;
    --orange-deep: #e8540e;
    --red-deep: #e00012;
    --badge-ring: #c9c9c9;
    --rule: #e4e4e4;
  }
  html, body {
    margin: 0;
    padding: 0;
    width: 960px;
    height: 1200px;
    overflow: hidden;
    background: var(--backdrop);
  }
  .values-sheet {
    position: absolute;
    left: 0;
    top: 229px;
    width: 960px;
    height: 741px;
    display: block;
  }
  .sheet-title {
    font-family: "Poppins", sans-serif;
    font-weight: 700;
    font-size: 165px;
    fill: var(--title-grey);
  }
  .badge-number {
    font-family: "Poppins", sans-serif;
    font-weight: 700;
    font-size: 19px;
    fill: var(--ink-dark);
  }
  .value-heading {
    font-family: "Poppins", sans-serif;
    font-weight: 800;
    font-size: 26px;
    fill: var(--ink-dark);
  }
  .value-point {
    font-family: "Poppins", sans-serif;
    font-weight: 400;
    font-size: 17.5px;
    fill: var(--text);
  }
  .bullet { fill: none; stroke: var(--orange); stroke-width: 2; }
  .brand-name {
    font-family: "Poppins", sans-serif;
    font-weight: 700;
    font-size: 52px;
    fill: var(--ink-dark);
  }
</style>
</head>
<body>
<svg class="values-sheet" viewBox="0 0 1246 962" xmlns="http://www.w3.org/2000/svg">
  <!-- base areas -->
  <rect class="paper" x="0" y="0" width="1246" height="962" fill="var(--paper)"/>
  <rect class="dark-field" x="0" y="0" width="1129" height="355" fill="var(--ink-dark)"/>
  <rect class="dark-strip" x="0" y="0" width="129" height="962" fill="var(--ink-dark)"/>

  <text class="sheet-title" x="606" y="181" text-anchor="middle" textLength="895" lengthAdjust="spacingAndGlyphs">Our Values</text>

  <!-- white wells inside the wave -->
  <g class="wells" fill="var(--paper)">
    <circle cx="229" cy="355" r="86"/>
    <circle cx="429" cy="355" r="86"/>
    <circle cx="629" cy="355" r="86"/>
    <circle cx="829" cy="355" r="86"/>
    <circle cx="1029" cy="355" r="86"/>
  </g>

  <!-- the wave ribbon -->
  <g class="wave" fill="none" stroke-width="33">
    <path d="M129 962 V355 A100 100 0 0 1 329 355" stroke="var(--amber)"/>
    <path d="M329 355 A100 100 0 0 0 529 355" stroke="var(--orange)"/>
    <path d="M529 355 A100 100 0 0 1 729 355" stroke="var(--red)"/>
    <path d="M729 355 A100 100 0 0 0 929 355" stroke="var(--amber)"/>
    <path d="M929 355 A100 100 0 0 1 1129 355 V0" stroke="var(--orange)"/>
  </g>

  <!-- value icon discs -->
  <circle class="icon-disc" cx="229" cy="355" r="68" fill="var(--amber-deep)" role="img" aria-label="Icon of a person helping another with a speech bubble"/>
  <circle class="icon-disc" cx="429" cy="355" r="68" fill="var(--orange-deep)" role="img" aria-label="Icon of open hands holding a heart"/>
  <circle class="icon-disc" cx="629" cy="355" r="68" fill="var(--red-deep)" role="img" aria-label="Icon of a hand holding a heart"/>
  <circle class="icon-disc" cx="829" cy="355" r="68" fill="var(--amber-deep)" role="img" aria-label="Icon of a group of people"/>
  <circle class="icon-disc" cx="1029" cy="355" r="68" fill="var(--orange-deep)" role="img" aria-label="Icon of a raised fist"/>

  <!-- number badges -->
  <g class="badges" fill="var(--paper)" stroke="var(--badge-ring)" stroke-width="3">
    <circle cx="229" cy="250" r="23"/>
    <circle cx="429" cy="456" r="23"/>
    <circle cx="629" cy="250" r="23"/>
    <circle cx="829" cy="456" r="23"/>
    <circle cx="1029" cy="250" r="23"/>
  </g>
  <g text-anchor="middle">
    <text class="badge-number" x="229" y="257">01</text>
    <text class="badge-number" x="429" y="463">02</text>
    <text class="badge-number" x="629" y="257">03</text>
    <text class="badge-number" x="829" y="463">04</text>
    <text class="badge-number" x="1029" y="257">05</text>
  </g>

  <!-- headings -->
  <g text-anchor="middle">
    <text class="value-heading" x="229" y="457">BE</text>
    <text class="value-heading" x="229" y="485">HELPFUL</text>
    <text class="value-heading" x="429" y="507">BE</text>
    <text class="value-heading" x="429" y="535">HUMBLE</text>
    <text class="value-heading" x="629" y="457">BE</text>
    <text class="value-heading" x="629" y="485">HONEST</text>
    <text class="value-heading" x="829" y="507">BE</text>
    <text class="value-heading" x="829" y="535">HUMAN</text>
    <text class="value-heading" x="1029" y="457">BE</text>
    <text class="value-heading" x="1029" y="485">COURAGEOUS</text>
  </g>

  <!-- be helpful -->
  <g class="value-points">
    <circle class="bullet" cx="178" cy="513" r="2.6"/>
    <text class="value-point" x="188"><tspan x="188" y="519">Make every</tspan><tspan x="188" y="540">person and</tspan><tspan x="188" y="561">place better</tspan><tspan x="188" y="582">because you</tspan><tspan x="188" y="603">are there.</tspan></text>
    <circle class="bullet" cx="178" cy="636" r="2.6"/>
    <text class="value-point" x="188"><tspan x="188" y="642">Deliver wow</tspan><tspan x="188" y="663">with every</tspan><tspan x="188" y="684">interaction.</tspan></text>
  </g>

  <!-- be humble -->
  <g class="value-points">
    <circle class="bullet" cx="375" cy="565" r="2.6"/>
    <text class="value-point"><tspan x="385" y="571">Listen with</tspan><tspan x="385" y="589">every muscle.</tspan></text>
    <circle class="bullet" cx="375" cy="616" r="2.6"/>
    <text class="value-point"><tspan x="385" y="622">Passionately</tspan><tspan x="385" y="640">help others first.</tspan></text>
    <circle class="bullet" cx="375" cy="668" r="2.6"/>
    <text class="value-point"><tspan x="385" y="674">Seek first to</tspan><tspan x="385" y="692">understand.</tspan></text>
  </g>

  <!-- be honest -->
  <g class="value-points">
    <circle class="bullet" cx="578" cy="513" r="2.6"/>
    <text class="value-point"><tspan x="588" y="519">Earn trust</tspan><tspan x="588" y="540">every day.</tspan></text>
    <circle class="bullet" cx="578" cy="575" r="2.6"/>
    <text class="value-point"><tspan x="588" y="581">Be open and</tspan><tspan x="588" y="602">direct.</tspan></text>
    <circle class="bullet" cx="578" cy="637" r="2.6"/>
    <text class="value-point"><tspan x="588" y="643">Treat everyone</tspan><tspan x="588" y="664">with fairness</tspan><tspan x="588" y="685">and respect.</tspan></text>
  </g>

  <!-- be human -->
  <g class="value-points">
    <circle class="bullet" cx="781" cy="565" r="2.6"/>
    <text class="value-point"><tspan x="791" y="571">Celebrate</tspan><tspan x="791" y="589">passion and</tspan><tspan x="791" y="608">action.</tspan></text>
    <circle class="bullet" cx="781" cy="633" r="2.6"/>
    <text class="value-point"><tspan x="791" y="639">Create an</tspan><tspan x="791" y="658">environment</tspan><tspan x="791" y="677">where people</tspan><tspan x="791" y="696">are authentic.</tspan></text>
    <circle class="bullet" cx="781" cy="720" r="2.6"/>
    <text class="value-point"><tspan x="791" y="726">Hire great people</tspan><tspan x="791" y="744">and expect a lot</tspan><tspan x="791" y="762">from them</tspan></text>
  </g>

  <!-- be courageous -->
  <g class="value-points">
    <circle class="bullet" cx="973" cy="513" r="2.6"/>
    <text class="value-point"><tspan x="983" y="519">Dare mighty</tspan><tspan x="983" y="540">things.</tspan></text>
    <circle class="bullet" cx="973" cy="575" r="2.6"/>
    <text class="value-point"><tspan x="983" y="581">Make and honor</tspan><tspan x="983" y="602">commitments.</tspan></text>
    <circle class="bullet" cx="973" cy="637" r="2.6"/>
    <text class="value-point"><tspan x="983" y="643">All great things</tspan><tspan x="983" y="664">start with a</tspan><tspan x="983" y="685">small act of</tspan><tspan x="983" y="705">courage applied</tspan><tspan x="983" y="726">at the right</tspan><tspan x="983" y="746">moment.</tspan></text>
  </g>

  <!-- brand sign-off -->
  <line class="footer-rule" x1="444" y1="793" x2="804" y2="793" stroke="var(--rule)" stroke-width="1.5"/>
  <circle class="brand-dot" cx="483" cy="842" r="34" fill="var(--orange)"/>
  <text class="brand-name" x="544" y="860">BrisKel</text>
</svg>
</body>
</html>
```